Mental Health Non-profit Website that takes donations

We are a faith friendly non profit mental health agency. We need an about us section, a section for taking donations, and a place to list all our therapists and a photo of them
Unfortunately, many of our neighbors in Ohio face mental health challenges which harm their quality of life. Thousands of Ohioans experience trauma, addiction, anxiety, and depression, and the negative outcomes of these experiences continue to grow. While we know that data-driven counseling can improve quality of life for those with mental health challenges, many face economic and social barriers to accessing this transformational care.
Lanterns of Calm crosses barriers to mental health care for Ohioans. We are a nonprofit team of counselors dedicated to employing best practices in modes accessible to people of all backgrounds. A trauma-informed, faith-sensitive methodology uniquely equips us to address holistic mental health challenges. Donor support and community partnerships allow us to meet and serve individuals who could not otherwise access professional care.

Target Market(s)

Those seeking mental health therapy

Industry/Entity Type

Mental Health Non-profit

Coding

Coded - Design and coding required

Colors

Designer to choose colors to be used in the design.

Requirements
Must have
• Our logo colors of navy blue and gold, our logo, about us section, our mission section, a place to accept donations page for all of our therapists and their pictures, and a place for blog posts

```html
<!DOCTYPE html>
<html lang="en">
<head>
<meta charset="UTF-8">
<title>Lanterns of Calm Behavioral Health</title>
<link rel="stylesheet" href="https://fonts.googleapis.com/css2?family=Lexend:wght@300;400;500;600;700;800&display=swap">
<style>
:root{
  --navy:#0a1a48;
  --navy-deep:#021543;
  --gold:#c9a13e;
  --cream:#f3ecdf;
  --ink:#1d1d1f;
  --text:#2a2a2a;
  --white:#ffffff;
  --black:#050505;
  --rule:#2c2c2c;
}
*{box-sizing:border-box;margin:0;padding:0}
html,body{width:1200px;height:4211px;overflow:hidden}
body{font-family:'Lexend',sans-serif;color:var(--text);background:var(--white);position:relative}
section,header,footer{position:absolute;left:0;width:1200px}
.abs{position:absolute}
.center{text-align:center}

/* Hero */
.hero{top:0;height:576px;overflow:hidden}
.hero-photo{position:absolute;inset:0;background:
  radial-gradient(ellipse 70% 14% at 45% 47%,rgba(190,208,190,.75),rgba(190,208,190,0) 70%),
  linear-gradient(180deg,#101a14 0%,#22342a 12%,#34503c 24%,#4e6c52 34%,#7f9a86 42%,#a9bba6 47%,#8ea27c 53%,#6d8a45 62%,#5c7d2e 74%,#4a6a24 88%,#3e5a20 100%)}
.hero-shade{position:absolute;inset:0;background:linear-gradient(180deg,rgba(0,0,0,.5) 0%,rgba(0,0,0,.08) 28%,rgba(0,0,0,0) 100%)}
.brand{left:140px;top:16px;display:flex;flex-direction:column;align-items:center;width:145px}
.brand-mark{width:74px;height:74px;border-radius:50%;background:var(--gold)}
.brand-name{margin-top:12px;color:var(--gold);font-weight:600;font-size:12px;letter-spacing:.5px;text-align:center;line-height:1.2}
.topbar-phone{left:745px;top:20px;color:var(--white);font-size:11px;display:flex;align-items:center;gap:6px}
.topbar-phone b{font-weight:600}
.social-top{top:14px;width:26px;height:26px;border:1.5px solid var(--white);border-radius:50%}
.nav{left:0;top:74px;width:1200px;color:var(--white);font-size:12px}
.btn-contact{left:932px;top:62px;width:126px;height:39px;border-radius:20px;background:var(--gold);color:var(--white);font-size:12px;display:flex;align-items:center;justify-content:center}
.hero-title{top:294px;width:1200px;color:var(--white);font-weight:800;font-size:28px;letter-spacing:1px}
.hero-sub{top:335px;width:1200px;color:var(--white);font-size:15px;letter-spacing:.4px}
.btn-navy{background:var(--navy-deep);color:var(--white);border-radius:22px;display:flex;align-items:center;justify-content:center;font-size:13px}
.hero-btn{left:508px;top:374px;width:184px;height:40px;border:1px solid rgba(255,255,255,.5)}

/* About */
.about{top:576px;height:688px;background:var(--cream)}
.about-photo{left:140px;top:132px;width:252px;height:458px;border-radius:14px;background:
  radial-gradient(ellipse 45% 30% at 40% 55%,#9fb2cc 0%,rgba(159,178,204,0) 100%),
  linear-gradient(100deg,#5b4a40 0%,#d7d2c8 18%,#eae6df 45%,#f2efe9 70%,#ddd6cb 100%);box-shadow:0 6px 14px rgba(0,0,0,.12)}
.emblem{width:34px;height:34px;border-radius:50%;background:var(--navy)}
.about-emblem{left:625px;top:122px}
.about-kicker{left:625px;top:170px;font-size:17px;letter-spacing:1.8px;color:var(--ink)}
.about-title{left:625px;top:200px;width:480px;color:var(--gold);font-weight:600;font-size:33px;line-height:36px;letter-spacing:.3px}
.about-copy{left:625px;top:276px;width:432px;font-size:12.3px;line-height:25.3px;color:var(--ink);letter-spacing:.35px}
.about-copy p+p{margin-top:10px}

/* Section headings */
.sec-emblem{left:583px}
.sec-title{width:1200px;color:var(--gold);font-weight:600;font-size:31px;letter-spacing:1px}

/* Mission */
.mission{top:1264px;height:696px}
.mission-panel{top:417px;width:564px;height:243px}
.mission-panel.navy{left:0;background:var(--navy-deep);border-radius:0 18px 18px 0}
.mission-panel.gold{left:636px;background:var(--gold);border-radius:18px 0 0 18px}
.mission-photo{top:212px;width:381px;height:254px;border-radius:14px}
.mission-head{top:497px;width:381px;font-weight:500;font-size:15px}
.mission-body{top:533px;width:381px;font-size:12.5px;line-height:18px}

/* Therapists */
.team{top:1960px;height:620px}
.team-card{top:182px;width:290px;height:379px;border:1px solid var(--navy);border-radius:16px;background:var(--white)}
.team-card.featured{background:var(--gold);border-color:var(--gold)}
.avatar{left:92px;top:32px;width:106px;height:106px;border-radius:50%}
.card-name{top:170px;width:100%;font-weight:600;font-size:14.5px;color:var(--ink)}
.card-text{top:206px;left:25px;width:240px;font-size:12.8px;line-height:18.3px;color:var(--ink)}
.arrow{width:34px;height:34px;border-radius:50%;display:flex;align-items:center;justify-content:center}
.arrow.prev{left:78px;background:#c9c9c9}
.arrow.next{left:1088px;background:var(--gold)}

/* Blog */
.blog{top:2580px;height:575px}
.post{top:203px;width:282px;height:340px;border:1px solid var(--gold);border-radius:16px}
.post-photo{left:20px;top:-36px;width:241px;height:189px;border-radius:14px}
.post-title{top:180px;width:100%;font-weight:600;font-size:15px;color:var(--ink)}
.post-text{top:212px;left:26px;width:230px;font-size:12.8px;line-height:18.5px;color:var(--ink)}

/* Donate */
.donate{top:3155px;height:648px;overflow:hidden}
.donate-photo{position:absolute;inset:0;background:
  radial-gradient(ellipse 40% 14% at 48% 82%,rgba(150,112,84,.85),rgba(150,112,84,0) 80%),
  linear-gradient(180deg,#ffffff 0%,#f3f4f1 14%,#dfe3da 32%,#c3cab8 50%,#b7bca7 62%,#cdb29a 76%,#d8bfa6 86%,#aebbc0 100%)}
.donate-pill{left:140px;top:68px;width:918px;height:174px;border-radius:87px;background:var(--gold)}
.donate-title{top:34px;width:100%;font-weight:500;font-size:25px;color:var(--navy-deep)}
.donate-sub{top:73px;width:100%;font-weight:500;font-size:17px;color:var(--white);letter-spacing:.6px}
.donate-btn{left:382px;top:114px;width:155px;height:39px;font-size:12.5px}

/* Footer */
.footer{top:3803px;height:408px;background:var(--black);color:var(--white)}
.foot-brand{left:140px;top:80px;width:213px;display:flex;flex-direction:column;align-items:center}
.foot-brand .brand-mark{width:120px;height:120px}
.foot-brand .brand-name{font-size:17px;margin-top:16px}
.foot-head{top:92px;font-weight:500;font-size:14px;letter-spacing:.8px}
.foot-links{left:410px;top:135px;font-size:12.5px;line-height:31.5px}
.foot-links li{list-style:none}
.foot-links li::before{content:"»";margin-right:6px;font-size:11px}
.foot-social{left:625px;font-size:12.5px;display:flex;align-items:center;gap:12px;letter-spacing:.3px}
.foot-social i{display:block;width:27px;height:27px;border:1.5px solid var(--white);border-radius:50%}
.foot-contact{left:847px;font-size:12.5px;line-height:20px;display:flex;gap:10px}
.foot-contact svg{flex:none;margin-top:4px}
.foot-rule{left:0;top:355px;width:1200px;height:1px;background:var(--rule)}
.copyright{left:143px;top:376px;font-size:11px}
.legal{left:861px;top:376px;font-size:11px}
</style>
</head>
<body>

<header class="hero">
  <div class="hero-photo" role="img" aria-label="Photo of a woman sitting on a wooden bench by a forest lake"></div>
  <div class="hero-shade"></div>

  <div class="abs brand">
    <span class="brand-mark"></span>
    <span class="brand-name">LANTERNS OF CALM<br>BEHAVIORAL HEALTH</span>
  </div>

  <div class="abs topbar-phone">
    <svg width="12" height="12" viewBox="0 0 24 24" fill="none" stroke="#fff" stroke-width="2"><path d="M5 3h4l2 5-3 2a12 12 0 0 0 6 6l2-3 5 2v4a2 2 0 0 1-2 2A17 17 0 0 1 3 5a2 2 0 0 1 2-2z"/></svg>
    <span><b>Phone:</b> +44 123-555-0147</span>
  </div>
  <span class="abs social-top" style="left:929px"></span>
  <span class="abs social-top" style="left:963px"></span>
  <span class="abs social-top" style="left:997px"></span>
  <span class="abs social-top" style="left:1032px"></span>

  <nav class="abs nav">
    <span class="abs" style="left:660px">Home</span>
    <span class="abs" style="left:727px">About Us</span>
    <span class="abs" style="left:813px">Team</span>
    <span class="abs" style="left:877px">Blog</span>
  </nav>
  <div class="abs btn-contact">CONTACT US</div>

  <h1 class="abs hero-title center">A GUIDE TO BETTER MENTAL HEALTH</h1>
  <p class="abs hero-sub center">Steps Toward Mental Health Awareness</p>
  <div class="abs btn-navy hero-btn">CONTACT US TODAY</div>
</header>

<section class="about">
  <div class="abs about-photo" role="img" aria-label="Photo of a woman meditating cross-legged on a sofa"></div>
  <span class="abs emblem about-emblem"></span>
  <p class="abs about-kicker">About Lanterns of Calm</p>
  <h2 class="abs about-title">COMPASSIONATE CARE WHEN YOU NEED IT MOST</h2>
  <div class="abs about-copy">
    <p>Lanterns of Calm crosses barriers to mental health care for Ohioans. We are a nonprofit team of counselors dedicated to employing best practices in modes accessible to people of all backgrounds. A trauma-informed, faith-sensitive methodology uniquely equips us to address holistic mental health challenges. Donor support and community partnerships allow us to meet and serve individuals who could not otherwise access professional care.</p>
    <p>The following narrative introduces Lanterns of Calm and shares how community members, faith communities, and fellow agencies can partner in making this impactful expansion possible.</p>
  </div>
</section>

<section class="mission">
  <span class="abs emblem sec-emblem" style="top:87px"></span>
  <h2 class="abs sec-title center" style="top:143px">OUR MISSION</h2>

  <div class="abs mission-panel navy"></div>
  <div class="abs mission-photo" style="left:162px;background:radial-gradient(ellipse 35% 45% at 70% 60%,#b9a88e 0%,rgba(185,168,142,0) 100%),linear-gradient(100deg,#7a6d62 0%,#e4e3df 22%,#eeeeec 55%,#d8d4cc 80%,#9c9286 100%)" role="img" aria-label="Photo of a distressed young woman sitting on the floor"></div>
  <h3 class="abs mission-head center" style="left:162px;color:var(--white)">Trauma-Informed</h3>
  <p class="abs mission-body center" style="left:162px;color:var(--white)">All of our counselors have experience with trauma-informed methodology and seek to understand clients' present mental health challenges through the lens of past adverse circumstances.</p>

  <div class="abs mission-panel gold"></div>
  <div class="abs mission-photo" style="left:656px;background:radial-gradient(ellipse 30% 40% at 25% 55%,#f1eee8 0%,rgba(241,238,232,0) 100%),linear-gradient(110deg,#d9d3c8 0%,#c4a57c 38%,#6b5442 58%,#3e4a3e 80%,#6d5a45 100%)" role="img" aria-label="Photo of a counselor holding hands with a young client"></div>
  <h3 class="abs mission-head center" style="left:656px;color:var(--ink)">Faith-Sensitive</h3>
  <p class="abs mission-body center" style="left:656px;color:var(--ink)">Many individuals experiencing mental health challenges have adopted unhealthy spiritual attitudes (e.g., "God must hate me"). Our counselors are comfortable navigating these issues with clients who initiate such conversations.</p>
</section>

<section class="team">
  <span class="abs emblem sec-emblem" style="top:55px"></span>
  <h2 class="abs sec-title center" style="top:111px">MEET OUR THERAPISTS</h2>

  <div class="abs arrow prev" style="top:355px"><svg width="16" height="12" viewBox="0 0 16 12" fill="none" stroke="#fff" stroke-width="1.6"><path d="M15 6H1M6 1 1 6l5 5"/></svg></div>

  <article class="abs team-card" style="left:140px">
    <div class="abs avatar" style="background:radial-gradient(circle at 50% 45%,#e0c3ad 0%,#c9b0a0 40%,#d9d7d4 75%)" role="img" aria-label="Portrait photo of a therapist"></div>
    <h3 class="abs card-name center">Name of the Person</h3>
    <p class="abs card-text center">Lorem ipsum dolor sit amet, consectetuer adipiscing elit, sed diam nonummy nibh euismod tincidunt ut laoreet dolore magna aliquam erat volutpat. Ut wisi enim ad minim veniam, quis nostrud exerci tation ullamcorper.</p>
  </article>
  <article class="abs team-card featured" style="left:455px">
    <div class="abs avatar" style="background:radial-gradient(circle at 50% 48%,#e8c9b2 0%,#b98e62 45%,#d6c9b8 80%)" role="img" aria-label="Portrait photo of a therapist"></div>
    <h3 class="abs card-name center">Name of the Person</h3>
    <p class="abs card-text center">Lorem ipsum dolor sit amet, consectetuer adipiscing elit, sed diam nonummy nibh euismod tincidunt ut laoreet dolore magna aliquam erat volutpat. Ut wisi enim ad minim veniam, quis nostrud exerci tation ullamcorper.</p>
  </article>
  <article class="abs team-card" style="left:770px">
    <div class="abs avatar" style="background:radial-gradient(circle at 50% 45%,#e6cbb8 0%,#c7aa96 40%,#dcdad7 75%)" role="img" aria-label="Portrait photo of a therapist"></div>
    <h3 class="abs card-name center">Name of the Person</h3>
    <p class="abs card-text center">Lorem ipsum dolor sit amet, consectetuer adipiscing elit, sed diam nonummy nibh euismod tincidunt ut laoreet dolore magna aliquam erat volutpat. Ut wisi enim ad minim veniam, quis nostrud exerci tation ullamcorper.</p>
  </article>

  <div class="abs arrow next" style="top:355px"><svg width="16" height="12" viewBox="0 0 16 12" fill="none" stroke="#fff" stroke-width="1.6"><path d="M1 6h14M10 1l5 5-5 5"/></svg></div>
</section>

<section class="blog">
  <span class="abs emblem sec-emblem" style="top:37px"></span>
  <h2 class="abs sec-title center" style="top:92px">OUR BLOG</h2>

  <div class="abs arrow prev" style="top:356px"><svg width="16" height="12" viewBox="0 0 16 12" fill="none" stroke="#fff" stroke-width="1.6"><path d="M15 6H1M6 1 1 6l5 5"/></svg></div>

  <article class="abs post" style="left:140px">
    <div class="abs post-photo" style="background:radial-gradient(ellipse 30% 40% at 70% 60%,#4a5a48 0%,rgba(74,90,72,0) 100%),linear-gradient(105deg,#e9e6e0 0%,#d7c8b2 30%,#a68462 50%,#3d3a36 75%,#5b4d40 100%)" role="img" aria-label="Photo of a counseling session in an office"></div>
    <h3 class="abs post-title center">Lorem ipsum dolor sit amet</h3>
    <p class="abs post-text center">Lorem ipsum dolor sit amet, consectetuer adipiscing elit, sed diam nonummy nibh euismod tincidunt ut laoreet dolore magna aliquam erat volutpat.</p>
  </article>
  <article class="abs post" style="left:459px">
    <div class="abs post-photo" style="background:radial-gradient(ellipse 30% 45% at 50% 60%,#c7cdb4 0%,rgba(199,205,180,0) 100%),linear-gradient(100deg,#4c514b 0%,#8e9889 25%,#bfc4b3 50%,#6f7567 72%,#2f3438 100%)" role="img" aria-label="Photo of a group support session"></div>
    <h3 class="abs post-title center">Lorem ipsum dolor sit amet</h3>
    <p class="abs post-text center">Lorem ipsum dolor sit amet, consectetuer adipiscing elit, sed diam nonummy nibh euismod tincidunt ut laoreet dolore magna aliquam erat volutpat.</p>
  </article>
  <article class="abs post" style="left:777px">
    <div class="abs post-photo" style="background:radial-gradient(ellipse 30% 40% at 78% 55%,#eef0f2 0%,rgba(238,240,242,0) 100%),linear-gradient(100deg,#5d5a57 0%,#8e8b88 30%,#a7a4a0 55%,#7b6a58 75%,#cfd2d6 100%)" role="img" aria-label="Photo of a patient with a clinician reviewing notes"></div>
    <h3 class="abs post-title center">Lorem ipsum dolor sit amet</h3>
    <p class="abs post-text center">Lorem ipsum dolor sit amet, consectetuer adipiscing elit, sed diam nonummy nibh euismod tincidunt ut laoreet dolore magna aliquam erat volutpat.</p>
  </article>

  <div class="abs arrow next" style="top:356px"><svg width="16" height="12" viewBox="0 0 16 12" fill="none" stroke="#fff" stroke-width="1.6"><path d="M1 6h14M10 1l5 5-5 5"/></svg></div>
</section>

<section class="donate">
  <div class="donate-photo" role="img" aria-label="Photo of hands holding soil with a green seedling"></div>
  <div class="abs donate-pill">
    <h2 class="abs donate-title center">Help Us Bring Hope to Those Who Need It Most</h2>
    <p class="abs donate-sub center">Give a Little, Change a Lot</p>
    <div class="abs btn-navy donate-btn">Donate Now</div>
  </div>
</section>

<footer class="footer">
  <div class="abs foot-brand">
    <span class="brand-mark"></span>
    <span class="brand-name">LANTERNS OF CALM<br>BEHAVIORAL HEALTH</span>
  </div>

  <h4 class="abs foot-head" style="left:410px">NAVIGATION BAR</h4>
  <ul class="abs foot-links">
    <li>Home</li><li>About Us</li><li>Team</li><li>Blog</li><li>Contact Us</li>
  </ul>

  <h4 class="abs foot-head" style="left:625px">STAY CONNECTED</h4>
  <div class="abs foot-social" style="top:140px"><i></i>Gatherly</div>
  <div class="abs foot-social" style="top:176px"><i></i>Chirpline</div>
  <div class="abs foot-social" style="top:213px"><i></i>Snapgrove</div>
  <div class="abs foot-social" style="top:251px"><i></i>Workbridge</div>

  <h4 class="abs foot-head" style="left:847px">CONTACT DETAILS</h4>
  <div class="abs foot-contact" style="top:128px">
    <svg width="11" height="13" viewBox="0 0 12 16" fill="#fff"><path d="M6 0a6 6 0 0 0-6 6c0 4.5 6 10 6 10s6-5.5 6-10a6 6 0 0 0-6-6zm0 8.5A2.5 2.5 0 1 1 6 3.5a2.5 2.5 0 0 1 0 5z"/></svg>
    <span>48 Willow Bend Road,<br>Maple Hollow, OH</span>
  </div>
  <div class="abs foot-contact" style="top:198px">
    <svg width="12" height="12" viewBox="0 0 24 24" fill="#fff"><path d="M5 2h4l2 5-3 2a12 12 0 0 0 6 6l2-3 5 2v4a2 2 0 0 1-2 2A17 17 0 0 1 3 4a2 2 0 0 1 2-2z"/></svg>
    <span>Phone<br>+44 123-555-0147</span>
  </div>
  <div class="abs foot-contact" style="top:248px">
    <svg width="12" height="10" viewBox="0 0 16 12" fill="#fff"><path d="M0 0h16v12H0z"/><path d="M0 0l8 6 8-6" stroke="#000" stroke-width="1.4" fill="none"/></svg>
    <span>Email<br>info@lanternsofcalm.org</span>
  </div>

  <div class="abs foot-rule"></div>
  <p class="abs copyright">Copyright © 2024 Lanterns of Calm. All Rights Reserved.</p>
  <p class="abs legal">Privacy Policy &nbsp;&nbsp;|&nbsp;&nbsp; Terms of Use</p>
</footer>

</body>
</html>
```